E-book cover for Varnok Pagelight. Requirments as follows: .jpg or .tif(f) file, at least 1000 pixels on the longest side, ideal image height/width ratio is 1.6 (example 1000 x 1600).

The book is called Pale Hollow and the author is Janet L Crowe. It's a horror novel about a town whose residents are driven mad by alien spores carried on the wind. I need to somehow represent wind on the cover eg, particles swirling around a town or around a tree. Maybe a tree on a hill with a town in the background?

```html
<!DOCTYPE html>
<html lang="en">
<head>
<meta charset="utf-8">
<title>Pale Hollow — Janet L. Crowe</title>
<link rel="stylesheet" href="https://fonts.googleapis.com/css2?family=Bebas+Neue&family=Teko:wght@400&display=swap">
<style>
  :root {
    --night: #000000;
    --mist: #f4fbfa;
    --spore-teal: #7fc4bb;
    --deep-teal: #2f6f69;
    --author-teal: #8ccbc2;
    --horizon-glow: #eef9f7;
  }
  html, body {
    margin: 0;
    padding: 0;
    background: var(--night);
    overflow: hidden;
  }
  .cover {
    position: relative;
    width: 815px;
    height: 1200px;
    background: var(--night);
    overflow: hidden;
  }
  .town-at-dusk {
    position: absolute;
    left: 0;
    top: 640px;
    width: 815px;
    height: 360px;
    background:
      radial-gradient(ellipse 52% 26% at 48% 36%, var(--horizon-glow) 0%, #b9e2dc 30%, rgba(90,160,152,0.85) 55%, rgba(20,45,43,0.6) 80%, rgba(0,0,0,0) 100%),
      linear-gradient(to bottom, rgba(0,0,0,0) 0%, rgba(14,34,32,0.9) 45%, #0a1716 62%, var(--night) 100%);
  }
  .artwork {
    position: absolute;
    inset: 0;
  }
  .title-line {
    font-family: "Bebas Neue", "Oswald", sans-serif;
  }
  .author-name {
    font-family: "Teko", "Oswald", sans-serif;
    font-weight: 400;
  }
</style>
</head>
<body>
<main class="cover">
  <div class="town-at-dusk" role="img" aria-label="Photograph of a quiet suburban street at dusk, rows of dark houses under a pale glowing teal horizon"></div>

  <svg class="artwork" width="815" height="1200" viewBox="0 0 815 1200" xmlns="http://www.w3.org/2000/svg">
    <defs>
      <linearGradient id="title-fill" x1="0" y1="0" x2="0" y2="1">
        <stop offset="0" stop-color="var(--mist)"/>
        <stop offset="0.45" stop-color="#d6eeea"/>
        <stop offset="0.8" stop-color="var(--spore-teal)"/>
        <stop offset="1" stop-color="var(--deep-teal)"/>
      </linearGradient>
      <linearGradient id="streak-fill" x1="0" y1="0" x2="0" y2="1">
        <stop offset="0" stop-color="#ffffff" stop-opacity="0"/>
        <stop offset="0.6" stop-color="#cfe6e2" stop-opacity="0.35"/>
        <stop offset="1" stop-color="#e8f5f3" stop-opacity="0.75"/>
      </linearGradient>
      <linearGradient id="author-fill" x1="0" y1="0" x2="0" y2="1">
        <stop offset="0" stop-color="#cde9e4"/>
        <stop offset="1" stop-color="var(--author-teal)"/>
      </linearGradient>
      <filter id="spore-grain" x="0" y="0" width="100%" height="100%">
        <feTurbulence type="fractalNoise" baseFrequency="0.95" numOctaves="2" seed="7" result="noise"/>
        <feColorMatrix in="noise" type="matrix" values="0 0 0 0 1  0 0 0 0 1  0 0 0 0 1  0 0 0 -2.2 1.35" result="speckle"/>
        <feComposite in="SourceGraphic" in2="speckle" operator="in"/>
      </filter>
    </defs>

    <g class="wind-streaks" filter="url(#spore-grain)">
      <rect x="150" y="110" width="100" height="330" fill="url(#streak-fill)"/>
      <rect x="260" y="20"  width="40"  height="200" fill="url(#streak-fill)"/>
      <rect x="335" y="0"   width="34"  height="200" fill="url(#streak-fill)"/>
      <rect x="420" y="0"   width="36"  height="210" fill="url(#streak-fill)"/>
      <rect x="475" y="110" width="50"  height="230" fill="url(#streak-fill)"/>
      <rect x="560" y="150" width="120" height="300" fill="url(#streak-fill)"/>
      <rect x="300" y="330" width="60"  height="300" fill="url(#streak-fill)" opacity="0.6"/>
    </g>

    <g class="book-title" fill="url(#title-fill)">
      <text class="title-line" x="407" y="335" text-anchor="middle" font-size="320" textLength="370" lengthAdjust="spacingAndGlyphs">PALE</text>
      <text class="title-line" x="407" y="615" text-anchor="middle" font-size="430" textLength="600" lengthAdjust="spacingAndGlyphs">HOLLOW</text>
    </g>

    <g class="title-dust" filter="url(#spore-grain)" opacity="0.55">
      <rect x="110" y="560" width="600" height="110" fill="url(#streak-fill)" transform="rotate(180 410 615)"/>
    </g>

    <text class="author-name" x="407" y="1128" text-anchor="middle" font-size="92" textLength="540" lengthAdjust="spacing" fill="url(#author-fill)">JANET L. CROWE</text>
  </svg>
</main>
</body>
</html>
```